palduro.org business card design

We need 2-sided business cards for palduro.org; one side will be printed in English (EN), the other in Spanish (ES); the information represnted will be the same.
We are a non-profit that aims to mentor and coach future leaders / visionaries. Our target markets are developing countries (Latin America, Africa, Asia) rather than the developed ("western") world. Our business model works by finding funding to mentor / coach a candidate. We provide several mentors / coaches per candidate which help translate the candidate's vision / dream into a path with objectives and steps.
We want the business cards to transmit our values, which are: innovation, learning / self-improvement, equality (i.e. free from discrimination), boldness, intelligence, thoughtfulness, culture, society, future, sustainability.
We recommend the designers work with these values to produce a bold and innovative design, which does not need to adhere to the traditional criteria for business cards. Please use fresh (modern) colours.

Target Market(s)

Visionaries and thought leaders all over the world, but initially in Latin America. We don't discriminate on age, sex, religion, race or any other difference between people

Industry/Entity Type

Leadership

Contact Information for Business Card

The business cards will contain one language (English / Spanish) per side. It would be nice to have some continuity between the front and the back (e.g. pattern, colours).
Each side will contain the company name, website (www.palduro.org) and a slogan / mantra (which will be provided and can be represented as a placeholder until such time). The other details will be Name, (Function), and contact details (email and phone number).

Font styles to use
Sans Serif

Colors

Designer to choose colors to be used in the design.

Requirements
Must have
• [Side A: ENGLISH --- COMPANY INFO]
• [Company Name] Palduro
• [Slogan / Mantra] Shape your world!
• [Website] palduro.org
• [Side A: ENGLISH --- PERSONAL INFO]
• [Name] Tim Hallox
• [Job Title] Mentoring Coordinator
• [Phone / WhatsApp] +51 917 208 386
• [eMail] tim@palduro.org
• [Side B: SPANISH --- COMPANY INFO]
• [Company Name] Palduro
• [Slogan / Mantra] ¡Moldea tu mundo!
• [Website] palduro.org
• [Side B: SPANISH --- PERSONAL INFO]
• [Name] Timothy Hallox
• [Job Title] Coordinador de Mentoreo
• [eMail] tim@palduro.org
• [SIDE A: ENGLISH --- Central Values]
• - Future
• - Growth
• - Leadership
• [SIDE B: SPANISH --- Central Values]
• - Futuro
• - Liderazgo
• - Crecimiento
Nice to have
• Innovative and different design. Modern and fresh. Bold and clever.
• Secondary Values (we would like represented) are:
• [SIDE A: ENGLISH --- Secondary Values]
• - Equality
• - Innovation
• - Sustainability
• [SIDE B: SPANISH --- Secondary Values]
• - Igualdad
• - Innovación
• - Sostenibilidad
Should not have
• Please note that the images I have attached to this brief are just some images that I liked while browsing for material for the website. It does not imply I want these colours or this type of design, just that I felt these images had a good feel.

```html
<!DOCTYPE html>
<html lang="en">
<head>
<meta charset="utf-8">
<title>Palduro business cards</title>
<link href="https://fonts.googleapis.com/css2?family=Open+Sans:wght@300;400;700&display=swap" rel="stylesheet">
<style>
  :root {
    --brand-blue: #1f82b9;
    --brand-green: #6cbf24;
    --card-dark: #020202;
    --card-light: #f2f2f2;
    --ink-dark: #333333;
    --ink-light: #ffffff;
    --backdrop: #e6e4e1;
  }
  * { margin: 0; padding: 0; box-sizing: border-box; }
  html, body {
    width: 1200px; height: 900px; overflow: hidden;
    background: var(--backdrop);
    font-family: "Open Sans", Arial, sans-serif;
  }
  .canvas { position: relative; width: 1200px; height: 900px; }

  .card {
    position: absolute; width: 600px; height: 343px; overflow: hidden;
    box-shadow: 0 6px 18px rgba(0,0,0,0.18);
  }
  .card--spanish { left: 70px; top: 90px; background: var(--card-dark); color: var(--ink-light); }
  .card--english { left: 530px; top: 467px; background: var(--card-light); color: var(--ink-dark); }

  .card__waves { position: absolute; inset: 0; width: 600px; height: 343px; }
  .wave-blue { fill: var(--brand-blue); }
  .wave-green { fill: var(--brand-green); }

  .holder { position: absolute; left: 40px; top: 40px; }
  .holder__name {
    font-weight: 700; font-size: 22px; letter-spacing: 0.3px;
    color: var(--brand-blue); text-transform: uppercase; line-height: 1.1;
  }
  .holder__role { font-size: 14px; line-height: 1.3; }

  .brand {
    position: absolute; right: 38px; top: 40px;
    display: flex; align-items: center; gap: 10px;
  }
  .brand__dot { width: 12px; height: 12px; border-radius: 50%; background: var(--brand-green); }
  .brand__name {
    font-weight: 300; font-size: 54px; line-height: 1;
    color: var(--brand-blue); letter-spacing: 1px;
  }

  .contacts { position: absolute; left: 40px; top: 132px; list-style: none; }
  .contacts__item {
    display: flex; align-items: center; gap: 7px;
    font-size: 16px; line-height: 22px;
  }
  .contacts__icon { width: 16px; height: 16px; flex: none; }
  .icon-disc { fill: var(--brand-blue); }
  .icon-mark { fill: none; stroke: #ffffff; stroke-width: 1.6; stroke-linecap: round; stroke-linejoin: round; }

  .values {
    position: absolute; left: 58px; top: 204px;
    font-size: 16px; line-height: 22px; display: flex; gap: 8px;
  }
  .values__divider { width: 2px; height: 20px; align-self: center; }
  .card--spanish .values__divider { background: var(--brand-green); }
  .card--english .values__divider { background: var(--brand-blue); }

  .slogan {
    position: absolute; right: 22px; top: 240px;
    font-size: 20px; line-height: 26px; color: var(--ink-light);
  }
</style>
</head>
<body>
<main class="canvas">

  <!-- Spanish side -->
  <section class="card card--spanish" lang="es">
    <svg class="card__waves" viewBox="0 0 600 343" aria-hidden="true">
      <path class="wave-green" d="M0,282 C130,284 280,268 395,238 C290,282 150,305 0,304 Z"/>
      <path class="wave-blue" d="M600,160 C520,168 450,200 400,240 C320,300 180,318 0,318 L0,343 L600,343 Z"/>
    </svg>
    <div class="holder">
      <p class="holder__name">Timothy Hallox</p>
      <p class="holder__role">Coordinador de Mentoreo</p>
    </div>
    <div class="brand">
      <span class="brand__name">Palduro</span>
      <span class="brand__dot"></span>
    </div>
    <ul class="contacts">
      <li class="contacts__item">
        <svg class="contacts__icon" viewBox="0 0 16 16"><circle class="icon-disc" cx="8" cy="8" r="8"/><path class="icon-mark" d="M4.5,11.5 L5.2,9.4 A3.6,3.6 0 1 1 6.6,10.8 Z"/></svg>
        +51 917 208 386
      </li>
      <li class="contacts__item">
        <svg class="contacts__icon" viewBox="0 0 16 16"><circle class="icon-disc" cx="8" cy="8" r="8"/><path class="icon-mark" d="M5.2,4.6 L6.6,4.6 L7.2,6.4 L6.3,7.2 C6.8,8.3 7.7,9.2 8.8,9.7 L9.6,8.8 L11.4,9.4 L11.4,10.8 C8,11 5,8 5.2,4.6 Z"/></svg>
        +51 917 208 386
      </li>
      <li class="contacts__item">
        <svg class="contacts__icon" viewBox="0 0 16 16"><circle class="icon-disc" cx="8" cy="8" r="8"/><rect class="icon-mark" x="4" y="5.3" width="8" height="5.6"/><path class="icon-mark" d="M4,5.3 L8,8.4 L12,5.3"/></svg>
        tim@palduro.org
      </li>
    </ul>
    <p class="values">
      <span>Crecimiento</span><span class="values__divider"></span>
      <span>Futuro</span><span class="values__divider"></span>
      <span>Liderazgo</span>
    </p>
    <p class="slogan">¡Moldea tu mundo!</p>
  </section>

  <!-- English side -->
  <section class="card card--english" lang="en">
    <svg class="card__waves" viewBox="0 0 600 343" aria-hidden="true">
      <path class="wave-green" d="M0,282 C130,284 280,268 395,238 C290,282 150,305 0,304 Z"/>
      <path class="wave-blue" d="M600,160 C520,168 450,200 400,240 C320,300 180,318 0,318 L0,343 L600,343 Z"/>
    </svg>
    <div class="holder">
      <p class="holder__name">Timothy Hallox</p>
      <p class="holder__role">Coordinator Mentoring</p>
    </div>
    <div class="brand">
      <span class="brand__name">Palduro</span>
      <span class="brand__dot"></span>
    </div>
    <ul class="contacts">
      <li class="contacts__item">
        <svg class="contacts__icon" viewBox="0 0 16 16"><circle class="icon-disc" cx="8" cy="8" r="8"/><path class="icon-mark" d="M4.5,11.5 L5.2,9.4 A3.6,3.6 0 1 1 6.6,10.8 Z"/></svg>
        +51 917 208 386
      </li>
      <li class="contacts__item">
        <svg class="contacts__icon" viewBox="0 0 16 16"><circle class="icon-disc" cx="8" cy="8" r="8"/><path class="icon-mark" d="M5.2,4.6 L6.6,4.6 L7.2,6.4 L6.3,7.2 C6.8,8.3 7.7,9.2 8.8,9.7 L9.6,8.8 L11.4,9.4 L11.4,10.8 C8,11 5,8 5.2,4.6 Z"/></svg>
        +51 917 208 386
      </li>
      <li class="contacts__item">
        <svg class="contacts__icon" viewBox="0 0 16 16"><circle class="icon-disc" cx="8" cy="8" r="8"/><rect class="icon-mark" x="4" y="5.3" width="8" height="5.6"/><path class="icon-mark" d="M4,5.3 L8,8.4 L12,5.3"/></svg>
        tim@palduro.org
      </li>
    </ul>
    <p class="values">
      <span>Growth</span><span class="values__divider"></span>
      <span>Future</span><span class="values__divider"></span>
      <span>Leadership</span>
    </p>
    <p class="slogan">Shape your world!</p>
  </section>

</main>
</body>
</html>
```